Multi Disciplinary Health Clinic Needs a Pop Up Banner

Brightway Health needs a pop up banner ( approx. 33" x 80") to use at marketing events. We offer Chiropractic, Massage Therapy, Acupuncture, Laser Therapy, Shockwave Therapy and a lot of other modalities. We have a diverse client base ranging from children to professional athletes. More info about our clinic can be found at www.brightwayhealth.ca

Target Market(s)

potential patients, all age ranges, people who are in pain or are wanting to improve their health

Industry/Entity Type

Health And Wellness

Font styles to use
Sans Serif

Requirements
Must have
• our logo
• serives: chiropractic, massage therapy, shockwave, laser
• our logo colours as the basis for the colour theme
• our website address
Nice to have
• our phone number
• images from our website ( i have high resolution files of all images)
• word font that fits with our logo font
Should not have
• an abundance of spa massage pictures. we focus more on the rehabilitation of pain and injury.

```html
<!DOCTYPE html>
<html lang="en">
<head>
<meta charset="utf-8">
<title>Brightway Health – Pop Up Banner</title>
<link rel="stylesheet" href="https://fonts.googleapis.com/css2?family=Orbitron:wght@500&family=Open+Sans:wght@400;600;700&display=swap">
<style>
  :root {
    --brand-blue: #1d67ad;
    --brand-grey: #5f6266;
    --photo-light: #b9bcc0;
    --photo-dark: #8d9094;
    --footer-band: #63666b;
    --page-bg: #e6e7e9;
    --white: #ffffff;
  }
  * { margin: 0; padding: 0; box-sizing: border-box; }
  html, body { width: 1200px; height: 960px; overflow: hidden; }
  body {
    background: var(--page-bg);
    font-family: "Open Sans", Arial, sans-serif;
    position: relative;
  }

  .banner {
    position: absolute;
    top: 70px;
    width: 338px;
    height: 820px;
    background: var(--white);
    overflow: hidden;
    box-shadow: 0 6px 20px rgba(0,0,0,0.18);
  }
  .banner--her { left: 90px; }
  .banner--him { left: 510px; }

  .brand-name {
    position: absolute;
    top: 62px;
    left: 0; right: 0;
    display: flex;
    align-items: center;
    justify-content: center;
    gap: 12px;
    font-size: 30px;
    font-weight: 600;
    color: var(--brand-blue);
    letter-spacing: 0.5px;
  }
  .brand-name__dot {
    width: 22px; height: 22px;
    border-radius: 50%;
    background: var(--brand-blue);
  }

  .tagline {
    position: absolute;
    top: 190px;
    left: 0; right: 0;
    text-align: center;
    font-family: "Orbitron", "Arial", sans-serif;
    font-weight: 500;
    line-height: 1.12;
  }
  .tagline__lead { display: block; font-size: 21px; color: var(--brand-blue); letter-spacing: 1px; }
  .tagline__strong { display: block; font-size: 31px; color: var(--brand-grey); margin-top: 4px; letter-spacing: 1px; }

  .photo {
    position: absolute;
    top: 300px;
    left: 0; right: 0;
    height: 440px;
  }
  .banner--her .photo { background: linear-gradient(100deg, #e9d9cf 0%, #d8c4b8 38%, var(--photo-light) 60%, var(--photo-dark) 100%); }
  .banner--him .photo { background: linear-gradient(260deg, #d9bfa9 0%, #c9ad96 40%, var(--photo-light) 62%, var(--photo-dark) 100%); }

  .services {
    position: absolute;
    top: 455px;
    list-style: none;
    font-size: 13.5px;
    color: var(--white);
    text-transform: uppercase;
  }
  .services__title, .services__more {
    color: var(--brand-blue);
    font-size: 17px;
    font-weight: 600;
  }
  .services__title { margin-bottom: 8px; }
  .services__more { margin-top: 6px; }
  .services__item {
    display: flex;
    align-items: center;
    gap: 10px;
    height: 27px;
  }
  .tick { width: 13px; height: 13px; flex: none; }

  .banner--her .services { right: 12px; text-align: right; }
  .banner--her .services__item { justify-content: flex-end; }
  .banner--him .services { left: 14px; }

  .footer-band {
    position: absolute;
    bottom: 0; left: 0; right: 0;
    height: 80px;
    background: var(--footer-band);
    color: var(--white);
    padding: 22px 16px 0;
  }
  .footer-band__note { font-size: 10px; }
  .footer-band__url { font-size: 19px; font-weight: 700; letter-spacing: 0.3px; }

  .presentation-label {
    position: absolute;
    top: 60px;
    left: 900px;
    text-align: center;
    color: #333538;
  }
  .presentation-label__brand {
    font-size: 26px;
    font-weight: 600;
    color: var(--brand-grey);
    margin-bottom: 26px;
  }
  .presentation-label__title { font-size: 29px; letter-spacing: 1px; }
  .presentation-label__size { font-size: 20px; color: #55585c; }
</style>
</head>
<body>

  <section class="banner banner--her">
    <div class="brand-name"><span class="brand-name__dot"></span>Brightway Health</div>
    <h1 class="tagline">
      <span class="tagline__lead">HELPING YOU<br>LIVE LIFE</span>
      <span class="tagline__strong">PAIN FREE!</span>
    </h1>
    <div class="photo" role="img" aria-label="Smiling woman with bare shoulders on a grey textured background"></div>
    <ul class="services">
      <li class="services__title">WE OFFER YOU :</li>
      <li class="services__item">Chiropractic Therapy <svg class="tick" viewBox="0 0 14 14"><circle cx="7" cy="7" r="7" fill="#1d67ad"/><path d="M3.8 7.2l2.2 2.2 4.3-4.6" stroke="#fff" stroke-width="1.8" fill="none"/></svg></li>
      <li class="services__item">Massage Therapy <svg class="tick" viewBox="0 0 14 14"><circle cx="7" cy="7" r="7" fill="#1d67ad"/><path d="M3.8 7.2l2.2 2.2 4.3-4.6" stroke="#fff" stroke-width="1.8" fill="none"/></svg></li>
      <li class="services__item">Acupuncture <svg class="tick" viewBox="0 0 14 14"><circle cx="7" cy="7" r="7" fill="#1d67ad"/><path d="M3.8 7.2l2.2 2.2 4.3-4.6" stroke="#fff" stroke-width="1.8" fill="none"/></svg></li>
      <li class="services__item">Laser Therapy <svg class="tick" viewBox="0 0 14 14"><circle cx="7" cy="7" r="7" fill="#1d67ad"/><path d="M3.8 7.2l2.2 2.2 4.3-4.6" stroke="#fff" stroke-width="1.8" fill="none"/></svg></li>
      <li class="services__item">Shockwave Therapy <svg class="tick" viewBox="0 0 14 14"><circle cx="7" cy="7" r="7" fill="#1d67ad"/><path d="M3.8 7.2l2.2 2.2 4.3-4.6" stroke="#fff" stroke-width="1.8" fill="none"/></svg></li>
      <li class="services__more">AND MANY MORE !</li>
    </ul>
    <footer class="footer-band">
      <p class="footer-band__note">For more information please visit:</p>
      <p class="footer-band__url">WWW.BRIGHTWAYHEALTH.CA</p>
    </footer>
  </section>

  <section class="banner banner--him">
    <div class="brand-name"><span class="brand-name__dot"></span>Brightway Health</div>
    <h1 class="tagline">
      <span class="tagline__lead">HELPING YOU<br>LIVE LIFE</span>
      <span class="tagline__strong">PAIN FREE!</span>
    </h1>
    <div class="photo" role="img" aria-label="Smiling young man in a navy shirt on a grey textured background"></div>
    <ul class="services">
      <li class="services__title">WE OFFER YOU :</li>
      <li class="services__item"><svg class="tick" viewBox="0 0 14 14"><circle cx="7" cy="7" r="7" fill="#1d67ad"/><path d="M3.8 7.2l2.2 2.2 4.3-4.6" stroke="#fff" stroke-width="1.8" fill="none"/></svg> Chiropractic Therapy</li>
      <li class="services__item"><svg class="tick" viewBox="0 0 14 14"><circle cx="7" cy="7" r="7" fill="#1d67ad"/><path d="M3.8 7.2l2.2 2.2 4.3-4.6" stroke="#fff" stroke-width="1.8" fill="none"/></svg> Massage Therapy</li>
      <li class="services__item"><svg class="tick" viewBox="0 0 14 14"><circle cx="7" cy="7" r="7" fill="#1d67ad"/><path d="M3.8 7.2l2.2 2.2 4.3-4.6" stroke="#fff" stroke-width="1.8" fill="none"/></svg> Acupuncture</li>
      <li class="services__item"><svg class="tick" viewBox="0 0 14 14"><circle cx="7" cy="7" r="7" fill="#1d67ad"/><path d="M3.8 7.2l2.2 2.2 4.3-4.6" stroke="#fff" stroke-width="1.8" fill="none"/></svg> Laser Therapy</li>
      <li class="services__item"><svg class="tick" viewBox="0 0 14 14"><circle cx="7" cy="7" r="7" fill="#1d67ad"/><path d="M3.8 7.2l2.2 2.2 4.3-4.6" stroke="#fff" stroke-width="1.8" fill="none"/></svg> Shockwave Therapy</li>
      <li class="services__more">AND MANY MORE !</li>
    </ul>
    <footer class="footer-band">
      <p class="footer-band__note">For more information please visit:</p>
      <p class="footer-band__url">WWW.BRIGHTWAYHEALTH.CA</p>
    </footer>
  </section>

  <aside class="presentation-label">
    <p class="presentation-label__brand">Brightway Health</p>
    <p class="presentation-label__title">BANNER DESIGN</p>
    <p class="presentation-label__size">SIZE : 33″ X 80″</p>
  </aside>

</body>
</html>
```